Kestrel School Build Sales Brochure

I am looking for a 4 page (Be printed as A3 and folded in half) A4 Brochure I have attached a word document with basic layout, wording and some photos I want included in the brochure. The word document is only a very rough rough guide. I am looking for a designer to really put together something unique and eye catching that will work in getting peoples attention when arriving through the post.

I have also attached a zip file with more photos that can be added to the the brochure should your design lend itself to it.

I have attached logo, business card and letterhead to give you an idea of company colours/ identity but don't feel restricted by this. The brochure is stand alone and there to bring in new customers

I have also posted a website contest for the above company and you can have a look at that informationa as well.

Pages 2-3 of Brochure can be treated as A3 to allow more flexibility when laying out those pages.

Good luck and I look forward to seeing the results.

I use www.quillpressworks.co.uk for my printing so templates / standards / formats for prinitng can be found there.
Updates

Dear All,

Further to your comments I have uploaded a .zip file with all photos from the word document.

As for the vector file I don't seem to have it but it was donw by a designer on artfolkhub I have asked them to send me a copy. As soon as I have it I will upload it.

The first design submitted was very poor, but I am sure much better is to follow.

Kind regards,

Dorian

Dear All,

Vector file for the logo has now been uploaded.

Kind regards,

Dorian

Dear All,

I am not really "feeling" any of the brochures submitted to date, I like some of the design ideas but something is not right. I believe this is because my brief is not quite right. You are producing what I asked for but having looked at it again I would like to make the following changes to the brief,

1. I think there is too much writing. I have uploaded a new word document with the only writing I want on the brochure. I think this will allow more space for photos / design.

The writing must appear on the following pages,

1. About Us - On The Front Page
2. Services we Provide -   On the front page or two middle pages
3. Client List :  On the back page.

2. The front page must have photos on. I would say two at minimum.

Thank you for your efforts so far, I look forward to recieving revised designs.
Kind regards,

Dorian

Target Market(s)

Will be sent by mail to schools within London and the South East to be read by Head Teachers, Premises Managers and Business Managers.

Industry/Entity Type

School

Requirements
Must have
• Schools recieve many many brochures and mail shots. Mine needs to stand out grab their attention. I have always heard that yellow is a good colour for attracting attention but you all probably know what works best.

Contact Information must be large-ish and clear on the front page.

Photos in word document must be used somewhere

Logo (Obviously)

Submissions must be of all pages otherwise they will be eliminated.
Should not have
• I don''t want before pictures on the front cover as I think it detracts and looks a but grubby.

```html
<!DOCTYPE html>
<html lang="en">
<head>
<meta charset="utf-8">
<title>Kestrel School Build – Brochure</title>
<link href="https://fonts.googleapis.com/css2?family=Inter:wght@300;400;600&display=swap" rel="stylesheet">
<style>
:root{
  --orange:#f8a51e;
  --ink:#3a3a3a;
  --muted:#555;
  --grey-panel:#e9e9eb;
  --white:#ffffff;
  --green:#3a9a3c;
  --heading-grey:#666;
}
*{box-sizing:border-box;margin:0;padding:0}
html,body{width:840px;height:1200px;overflow:hidden;background:var(--white)}
body{font-family:"Inter",Helvetica,Arial,sans-serif;color:var(--ink);position:relative}
.abs{position:absolute}
.orange{background:var(--orange)}
.photo{position:absolute}
.title{color:var(--white);font-weight:300;line-height:1;letter-spacing:-.5px}
.bullets{list-style:none;position:absolute;font-size:8.2px;color:var(--ink)}
.bullets li{display:flex;align-items:center;height:12.1px;white-space:nowrap}
.bullets li svg{width:9px;height:9px;margin-right:8px;flex:none}
.brand{position:absolute;display:flex;align-items:center;gap:6px;font-weight:600;color:var(--ink);white-space:nowrap}
.brand .mark{background:var(--orange);flex:none}
.details{position:absolute;font-size:7.8px;line-height:12px;color:var(--muted)}
.details strong{color:#222;font-weight:600}
.about{position:absolute;left:444px;top:470px;width:156px;font-size:7.6px;line-height:9.4px;color:var(--white);text-align:justify}
.about p+p{margin-top:9px}
.ba-frame{position:absolute;width:170px;height:121px;background:var(--white);border:1px solid #cfcfcf;overflow:hidden}
.ba-frame .corner{position:absolute;left:0;top:0;width:32px;height:32px}
.ba-frame .photo{left:6px;top:7px;right:6px;bottom:8px}
.ba-label{position:absolute;font-size:8px;color:var(--ink);display:flex;align-items:center;gap:6px}
.ba-label svg{width:9px;height:9px}
</style>
</head>
<body>

<svg width="0" height="0" style="position:absolute">
  <defs>
    <symbol id="bullet" viewBox="0 0 20 20">
      <circle cx="10" cy="10" r="10" fill="#3a9a3c"/>
      <circle cx="10" cy="10" r="8.5" fill="#5cb84a"/>
      <path d="M5 12 Q6 7 11 7 V4.5 L15.5 8.5 L11 12.5 V10 Q8 10 5 12Z" fill="#fff"/>
    </symbol>
  </defs>
</svg>

<!-- Back page: client list & contact -->
<section class="page back">
  <div class="abs orange" style="left:13px;top:16px;width:192px;height:185px"></div>
  <h2 class="abs title" style="left:46px;top:145px;font-size:23px">CLIENT LIST</h2>
  <div class="photo" role="img" aria-label="Black and white close-up photograph of a child looking sideways"
       style="left:260px;top:20px;width:160px;height:180px;background:radial-gradient(ellipse at 80% 40%,#f4f4f4,#d9d9d9 55%,#bcbcbc)"></div>

  <ul class="bullets" style="left:45px;top:225px">
    <li><svg><use href="#bullet"/></svg>Ashby Primary School</li>
    <li><svg><use href="#bullet"/></svg>Little Acorns Nursery</li>
    <li><svg><use href="#bullet"/></svg>Harbour Lane Nursery</li>
    <li><svg><use href="#bullet"/></svg>Hillcrest School</li>
    <li><svg><use href="#bullet"/></svg>Thomas Arden Primary</li>
    <li><svg><use href="#bullet"/></svg>Meridian School</li>
    <li><svg><use href="#bullet"/></svg>Elmbrook Primary School</li>
    <li><svg><use href="#bullet"/></svg>Larkfield School</li>
  </ul>
  <ul class="bullets" style="left:215px;top:225px">
    <li><svg><use href="#bullet"/></svg>Southmere Primary</li>
    <li><svg><use href="#bullet"/></svg>Mill Bridge Primary School</li>
    <li><svg><use href="#bullet"/></svg>Kingsgate Primary School</li>
    <li><svg><use href="#bullet"/></svg>Brookside Primary School</li>
    <li><svg><use href="#bullet"/></svg>Borough of Wexmoor</li>
    <li><svg><use href="#bullet"/></svg>Borough of Fenhurst</li>
    <li><svg><use href="#bullet"/></svg>Borough of Castlebridge</li>
    <li><svg><use href="#bullet"/></svg>Borough of Redmarsh</li>
  </ul>

  <div class="abs orange" style="left:13px;top:340px;width:192px;height:99px"></div>
  <h2 class="abs title" style="left:46px;top:368px;font-size:24px">CONTACT</h2>
  <p class="abs title" style="left:50px;top:390px;font-size:15.5px">INFORMATION</p>
  <div class="photo" role="img" aria-label="Blurred photograph of a hand holding a small key with a word printed on it"
       style="left:264px;top:345px;width:156px;height:95px;background:linear-gradient(90deg,#fff 0%,#e6e6e6 35%,#bdbdbd 60%,#f2f2f2 75%,#c8c8c8 90%,#eee)"></div>

  <div class="details" style="left:44px;top:460px">
    <strong>Kestrel School Build Limited</strong><br>
    Marlow Court, Fernhill Road, Ashcombe,<br>
    Kingsmere, Surrey , KT0 0AA
    <div style="margin-top:9px">Tel: 0845 000 4417<br>Fax: 0845 000 4417</div>
    <div style="margin-top:9px">Email: hello@kestrelschoolbuild.co.uk<br>Web: www.kestrelschoolbuild.co.uk</div>
  </div>
  <div class="brand" style="left:288px;top:541px;font-size:10px">
    <span class="mark" style="width:8px;height:8px"></span>Kestrel School Build
  </div>
</section>

<!-- Front page -->
<section class="page front">
  <div class="abs orange" style="left:420px;top:16px;width:407px;height:581px"></div>
  <div class="photo" role="img" aria-label="Photograph of refurbished school washroom with fish-painted vanity units"
       style="left:430px;top:218px;width:90px;height:179px;background:linear-gradient(180deg,#eef0f3 0%,#dfe3ea 45%,#2c3d78 60%,#3b5ea8 100%)"></div>
  <div class="photo" role="img" aria-label="Photograph of a new timber seating structure on a grass playground"
       style="left:527px;top:218px;width:90px;height:179px;background:linear-gradient(180deg,#6b9bd8 0%,#5b7a3e 35%,#c08c5a 65%,#6aa43a 100%)"></div>
  <div class="abs" style="left:626px;top:215px;width:201px;height:183px;background:#f5f6f8"></div>
  <div class="brand" style="left:646px;top:268px;font-size:15px">
    <span class="mark" style="width:13px;height:13px"></span>Kestrel School Build
  </div>
  <div class="details" style="left:650px;top:318px;font-size:9px;line-height:12px;color:var(--muted)">
    Tel: 0845 000 4417<br>web: www.kestrelschoolbuild.co.uk<br>email: hello@kestrelschoolbuild.co.uk
  </div>
  <h1 class="abs title" style="left:444px;top:433px;font-size:25px">ABOUT US</h1>
  <div class="about">
    <p>Kestrel provides construction, design and project management services to schools and the wider education sector.</p>
    <p>Our clients are our number one priority and will enjoy unrivalled levels of service, integrity and reliability. Our projects are carried out to the highest quality, at an agreed fixed cost and within the agreed time.</p>
  </div>
</section>

<!-- Inside left: services -->
<section class="page services">
  <div class="photo" role="img" aria-label="Photograph of a white tiled medical room with sink and cabinets"
       style="left:12px;top:609px;width:164px;height:211px;background:linear-gradient(180deg,#f2f2f0,#dcdcd8 70%,#c9c9c4)"></div>
  <div class="photo" role="img" aria-label="Photograph of a refurbished first aid room with yellow treatment couch"
       style="left:177px;top:609px;width:240px;height:211px;background:linear-gradient(180deg,#f4f3ee 0%,#e6e3d6 60%,#efd85a 85%,#d8d2bd)"></div>
  <div class="abs orange" style="left:12px;top:820px;width:236px;height:130px"></div>
  <h2 class="abs title" style="left:41px;top:872px;font-size:35px">SERVICE</h2>
  <p class="abs title" style="left:42px;top:903px;font-size:20px">WE PROVIDE</p>
  <div class="photo" role="img" aria-label="Photograph of an in-ground trampoline set in playground surfacing by a brick wall"
       style="left:248px;top:820px;width:169px;height:135px;background:linear-gradient(180deg,#7fa1c9 0%,#9b4a35 25%,#7c3a2a 45%,#3a3a3a 65%,#f0b020 80%,#333)"></div>
  <div class="photo" role="img" aria-label="Photograph of a refurbished school corridor with blue flooring"
       style="left:248px;top:955px;width:169px;height:230px;background:linear-gradient(180deg,#f3f1ea 0%,#e8e0c8 55%,#3d5890 80%,#2c4478)"></div>

  <ul class="bullets" style="left:40px;top:983px">
    <li><svg><use href="#bullet"/></svg>Design and Project Management Services</li>
    <li><svg><use href="#bullet"/></svg>New Builds and Extensions</li>
    <li><svg><use href="#bullet"/></svg>Refurbishment of all areas including</li>
    <li><svg><use href="#bullet"/></svg>Specialist Special Needs Rooms ,</li>
    <li><svg><use href="#bullet"/></svg>General buildings maintenance.</li>
    <li><svg><use href="#bullet"/></svg>Design and Project Management Services</li>
    <li><svg><use href="#bullet"/></svg>Playground design.</li>
    <li><svg><use href="#bullet"/></svg>Playground equipment, surfacing and</li>
    <li><svg style="visibility:hidden"><use href="#bullet"/></svg>bespoke structures</li>
    <li><svg><use href="#bullet"/></svg>Temporary buildings and classrooms</li>
  </ul>
  <div class="brand" style="left:48px;top:1140px;font-size:10px">
    <span class="mark" style="width:8px;height:8px"></span>Kestrel School Build
  </div>
</section>

<!-- Inside right: before & after -->
<section class="page before-after">
  <div class="abs" style="left:418px;top:608px;width:409px;height:584px;background:var(--grey-panel)"></div>
  <h2 class="abs" style="left:452px;top:638px;font-size:38px;font-weight:300;color:var(--heading-grey);line-height:1;letter-spacing:-1px">BEFORE</h2>
  <p class="abs" style="left:453px;top:668px;font-size:23px;font-weight:300;color:var(--heading-grey);line-height:1;letter-spacing:-.5px">&amp;AFTER</p>
  <p class="abs" style="left:748px;top:636px;font-size:48px;font-weight:300;color:#f0f0f2;line-height:1">1</p>

  <div class="ba-frame" style="left:453px;top:718px">
    <svg class="corner" viewBox="0 0 32 32"><path d="M0 0H32L0 32Z" fill="#f8a51e"/></svg>
    <div class="photo" role="img" aria-label="Before: bare tarmac playground" style="background:linear-gradient(180deg,#b9c6d8 0%,#8a8f88 45%,#5d5f61 100%)"></div>
  </div>
  <div class="ba-frame" style="left:632px;top:718px">
    <svg class="corner" viewBox="0 0 32 32"><path d="M0 0H32L0 32Z" fill="#f8a51e"/></svg>
    <div class="photo" role="img" aria-label="After: playground with lawn and timber seating" style="background:linear-gradient(180deg,#5d8ed6 0%,#9b6f44 45%,#5c8e2e 75%,#3f6a22)"></div>
  </div>
  <div class="ba-label" style="left:513px;top:846px"><svg><use href="#bullet"/></svg>Before</div>
  <div class="ba-label" style="left:697px;top:846px"><svg><use href="#bullet"/></svg>After</div>

  <div class="ba-frame" style="left:453px;top:867px">
    <svg class="corner" viewBox="0 0 32 32"><path d="M0 0H32L0 32Z" fill="#f8a51e"/></svg>
    <div class="photo" role="img" aria-label="Before: dated washroom with red tiled floor" style="background:linear-gradient(180deg,#e9dcae 0%,#ddd2a8 50%,#a9452a 80%,#8e3a24)"></div>
  </div>
  <div class="ba-frame" style="left:632px;top:867px">
    <svg class="corner" viewBox="0 0 32 32"><path d="M0 0H32L0 32Z" fill="#f8a51e"/></svg>
    <div class="photo" role="img" aria-label="After: refurbished washroom with blue floor" style="background:linear-gradient(180deg,#eef0f4 0%,#c7d0dc 50%,#4d9aa8 70%,#2f3f7a)"></div>
  </div>
  <div class="ba-label" style="left:513px;top:994px"><svg><use href="#bullet"/></svg>Before</div>
  <div class="ba-label" style="left:697px;top:994px"><svg><use href="#bullet"/></svg>After</div>

  <div class="ba-frame" style="left:453px;top:1011px">
    <svg class="corner" viewBox="0 0 32 32"><path d="M0 0H32L0 32Z" fill="#f8a51e"/></svg>
    <div class="photo" role="img" aria-label="Before: old toilet cubicles with yellow walls" style="background:linear-gradient(180deg,#b8a063 0%,#d8c27a 50%,#8a7540 100%)"></div>
  </div>
  <div class="ba-frame" style="left:632px;top:1011px">
    <svg class="corner" viewBox="0 0 32 32"><path d="M0 0H32L0 32Z" fill="#f8a51e"/></svg>
    <div class="photo" role="img" aria-label="After: new washroom with fish-painted vanity units" style="background:linear-gradient(180deg,#e8ecf2 0%,#c9d2de 45%,#2d3d78 70%,#3b66b0)"></div>
  </div>
  <div class="ba-label" style="left:513px;top:1140px"><svg><use href="#bullet"/></svg>Before</div>
  <div class="ba-label" style="left:697px;top:1140px"><svg><use href="#bullet"/></svg>After</div>
</section>

</body>
</html>
```